Concrete Construction Business Card design

We are a commercial concrete construction company based in Texas. a family owned business which our trade was passed down and taught by our grandfather whom we want represented in this design. our grandfathers nick name was "pepe" so we are wanting the letter G to be symbolized in some way with a red pepe . colors should be possibly a grey color back ground , green letter g and red pepe pepper , to be left for you to decide with integrity , concrete professionalism,and mexican heritage

Target Market(s)

general contractors, architects,inverstors, and engineers

Industry/Entity Type

Concrete

Contact Information for Business Card

Herrera Concrete Construction LLC, Dennis Herrera, 1872 Bramblewood Ln. Denton, TX 76209, (940)318-2746, dhslabworkllc48@quarrymail.net

```html
<!DOCTYPE html>
<html lang="en">
<head>
<meta charset="utf-8">
<title>Herrera Concrete Construction LLC — Business Card</title>
<link rel="stylesheet" href="https://fonts.googleapis.com/css2?family=Amaranth:wght@700&display=swap">
<style>
  :root {
    --grey-light: #f4f4f4;
    --grey-mid: #b9bcbc;
    --grey-dark: #6f7474;
    --brand-green: #3cf03a;
    --band-green: #2ef02a;
    --band-red: #e80a0a;
    --text-white: #f6f6f6;
    --text-shadow: #3a3a3a;
  }
  html, body {
    margin: 0;
    padding: 0;
    width: 1200px;
    height: 702px;
    overflow: hidden;
    background: #ffffff;
  }
  .card {
    position: relative;
    width: 1200px;
    height: 702px;
    overflow: hidden;
    font-family: "Amaranth", "Trebuchet MS", sans-serif;
    font-weight: 700;
    color: var(--text-white);
  }
  .card__backdrop {
    position: absolute;
    left: 0; top: 0;
    width: 1200px; height: 532px;
    background: radial-gradient(ellipse 620px 460px at 560px 250px,
      var(--grey-light) 0%, var(--grey-mid) 55%, var(--grey-dark) 100%);
  }
  .embossed {
    text-shadow: 2px 3px 0 var(--text-shadow), 0 0 2px var(--text-shadow);
  }
  .brand-mark {
    position: absolute;
    left: 420px; top: 200px;
    width: 300px;
    text-align: center;
    font-size: 76px;
    line-height: 1;
    color: var(--brand-green);
  }
  .contact-name {
    position: absolute;
    left: 722px; top: 92px;
    font-size: 43px;
    letter-spacing: 2px;
    line-height: 1;
  }
  .contact-phone {
    position: absolute;
    left: 746px; top: 146px;
    font-size: 38px;
    letter-spacing: 3px;
    line-height: 1;
  }
  .company-name {
    position: absolute;
    left: 0; top: 412px;
    width: 1172px;
    text-align: center;
    font-size: 45px;
    letter-spacing: 4px;
    line-height: 1;
    text-transform: uppercase;
  }
  .band {
    position: absolute;
    left: 0;
    width: 1200px;
    display: flex;
    align-items: center;
    justify-content: center;
  }
  .band--address {
    top: 532px; height: 77px;
    background: var(--band-green);
    font-size: 41px;
    letter-spacing: 3px;
  }
  .band--email {
    top: 609px; height: 93px;
    background: var(--band-red);
    font-size: 41px;
    letter-spacing: 3px;
    padding-right: 40px;
    box-sizing: border-box;
  }
</style>
</head>
<body>
  <main class="card">
    <div class="card__backdrop"></div>

    <div class="brand-mark">Herrera</div>

    <div class="contact-name embossed">Dennis Herrera</div>
    <div class="contact-phone embossed">(940)318-2746</div>

    <div class="company-name embossed">Herrera Concrete Construction LLC</div>

    <div class="band band--address embossed">1872 Bramblewood Ln. Denton, TX 76209</div>
    <div class="band band--email embossed">dhslabworkllc48@quarrymail.net</div>
  </main>
</body>
</html>
```